Clockharbour Homepage Banner 1060 W x 100 H

Please see the attached 'word' document (Also copied below)
Feel free to use any images or logos from our website.
www.clockharbour.com.au

Background:
We are an Australian based official watch distributor/online retailer of international watch brands.

We require a new banner ad (1060 W x 100 H) to replace the existing one on our homepage www.clockharbour.com.au & wish to convey the following information:
*(Please feel free to alter wording, include or exclude points below & generally take creative license (with commercial reality in mind). We sell some luxury watches, so it must look professional & maintain a luxury look & feel.)

Clockharbour Direct:
Revolutionising the retail watch market !

- Buy direct from the official distributor & get world competitive
online prices (with full international warranty, & all original
papers, box & invoice)

- Eliminate all risk of fakes & non-existent factory warranty from
'grey' market sellers

- Free worldwide delivery over A$300

- Order online & 'try-on' in the comfort of your own home.
If you're not 100% happy, just post it back for a full refund or
exchange within 30 days

- Prefer to see & try on before purchase? Visit one of our retail
partner stores.

*** Feel free to copy any images from our website
www.clockharbour.com.au
Updates

Target Market(s)

Luxury watches

Industry/Entity Type

Retail

Font styles to use
Sans Serif

Requirements
Must have
• Visual imagery, text
Nice to have
• Feel free to use your creativity...
Should not have
• Cheap looking or tacky images. We sell some luxury watches, so we need to keep a professional & luxury image.

```html
<!DOCTYPE html>
<html lang="en">
<head>
<meta charset="utf-8">
<title>Clockharbour Direct – Eliminate All Risk</title>
<link href="https://fonts.googleapis.com/css2?family=Lato:wght@400;700&display=swap" rel="stylesheet">
<style>
  :root {
    --white: #ffffff;
    --gold: #cbb68c;
    --sand: #d8c6a3;
    --navy: #0f2a5c;
    --watch-dark: #1b1c2a;
    --watch-gold: #8a6a3c;
  }
  * { margin: 0; padding: 0; box-sizing: border-box; }
  html, body {
    width: 1200px;
    height: 113px;
    overflow: hidden;
    background: var(--white);
  }
  .banner {
    position: relative;
    width: 1200px;
    height: 113px;
    background: var(--white);
    font-family: "Lato", Arial, sans-serif;
  }
  .watch-photo {
    position: absolute;
    left: 0;
    top: 0;
    width: 232px;
    height: 113px;
    background: radial-gradient(circle at 40% 55%, #2a2f48 0%, var(--watch-dark) 45%, var(--watch-gold) 72%, #c9a86e 85%, #e9e0cf 100%);
  }
  .headline {
    position: absolute;
    left: 251px;
    top: 0;
    height: 113px;
    display: flex;
    align-items: center;
    font-size: 41px;
    font-weight: 400;
    letter-spacing: 0.5px;
    color: var(--gold);
    white-space: nowrap;
  }
  .promise-panel {
    position: absolute;
    left: 744px;
    top: 0;
    width: 456px;
    height: 113px;
    background: var(--sand);
  }
  .shield-icon {
    position: absolute;
    left: 672px;
    top: 16px;
    width: 56px;
    height: 76px;
  }
  .promise-list {
    position: absolute;
    left: 813px;
    top: 3px;
    list-style: none;
    color: var(--navy);
    font-size: 19.5px;
    line-height: 26px;
    white-space: pre;
  }
  .promise-list li::before {
    content: "•";
    margin-right: 1px;
  }
</style>
</head>
<body>
  <div class="banner">
    <div class="watch-photo" role="img" aria-label="Close-up photograph of a luxury chronograph watch with gold case and dark blue dial"></div>

    <h1 class="headline">ELIMINATE ALL RISK</h1>

    <div class="promise-panel"></div>

    <svg class="shield-icon" viewBox="0 0 56 76" aria-hidden="true">
      <path d="M28 4 L52 14 V36 C52 54 42 66 28 72 C14 66 4 54 4 36 V14 Z" fill="var(--white)" stroke="var(--navy)" stroke-width="5" stroke-linejoin="round"/>
      <path d="M17 38 L25 46 L40 29" fill="none" stroke="var(--navy)" stroke-width="5" stroke-linecap="round" stroke-linejoin="round"/>
    </svg>

    <ul class="promise-list">
      <li>Directly  from the official distributor</li>
      <li>Try Before You Buy</li>
      <li>30 days  Money Back</li>
      <li>No fakes, No falce warranty</li>
    </ul>
  </div>
</body>
</html>
```